WEBSITE & LOGO for MEDICAL CILINC

BRAND NAME ( LUMORA) Medical clinic for intravenous (IV) vitamin hydration and wellness therapy. range of signature infusions and boosters are targeted at preventative health and wellness – essentially replenishing your body with the fluids and vitamins it needs to be in tip-top condition.

Blood testing
laboratory analysis
IV therapy
IV infusion drips
phlebotomy services
nurses for Home care services
Patient repatriation services to their countries
Hire of medical equipments including beds and wheel chairs

www.quellant.com
www.brisoclinic.com
http://fundoroplan.co.uk

All adults
18+ women and men.

No black color in the background
DNA double helix image should to be implemented in the design and logo.
the website should be easy to be used so the clients can add to the shopping cart
- select treatment or drips
- supplement
- book nurses
- book home visit
- book nurse for international home care journey

Colors
86cae7
33b8a4
e4daeb
f9d9e8
fefafc
fbd2d3
eee9f4
85acd3
0455a3

Requirements
Must have
• DNA Double helix in Java animation
injection icon for IV injection
Infusion Icon Bag for IV infusion
Analysis icon
phlebotomy services icon
Patient repatriation services icon
Hire of medical equipments icon

light background and water blue menu and buttons with highlights
Nice to have
• dynamic website where
IV injections scroll from side to side
IV infusion scroll from side to side.

```html
<!DOCTYPE html>
<html lang="en">
<head>
<meta charset="utf-8">
<title>Lumora – IV Wellness Clinic</title>
<link href="https://fonts.googleapis.com/css2?family=Lato:wght@400;700;900&display=swap" rel="stylesheet">
<style>
:root{
  --teal:#33b8a4;
  --sky:#86cae7;
  --lav:#eee9f4;
  --lilac:#e4daeb;
  --navy:#0455a3;
  --ink:#222;
  --grey:#777;
  --white:#fff;
  --footer:#0b0b0b;
  --red:#e0262b;
}
*{box-sizing:border-box;margin:0;padding:0}
html,body{width:1200px;height:4584px;overflow:hidden}
body{position:relative;background:var(--white);font-family:'Lato',sans-serif;color:var(--ink)}
.abs{position:absolute}
.btn{display:inline-block;background:var(--teal);color:var(--white);font-weight:700;font-size:12px;letter-spacing:.5px;border-radius:20px;padding:10px 24px;text-transform:uppercase}
.btn.pale{background:var(--lilac);color:#555}
.section-title{position:absolute;left:0;width:1200px;text-align:center;font-weight:900;font-size:38px;color:#111}
.section-title::after{content:"";display:block;width:60px;height:3px;background:var(--teal);margin:14px auto 0}

/* top bar */
.topbar{left:0;top:0;width:1200px;height:36px;background:var(--white)}
.topbar-accent{left:0;top:0;width:1200px;height:4px;background:var(--teal)}
.social{top:10px;width:24px;height:24px;border-radius:50%;border:2px solid var(--sky)}
.call{left:392px;top:14px;font-size:14px;color:#444}
.call b{color:#111}
.tab{top:0;width:200px;height:36px;background:var(--teal);color:var(--white);font-size:12px;font-weight:700;text-align:center;line-height:36px;border-radius:0 0 18px 18px}

/* nav */
.logo{left:112px;top:92px;font-size:26px;font-weight:900;color:#333;letter-spacing:1px}
.menu{left:460px;top:96px;display:flex;gap:40px;font-size:15px;color:#333}
.menu .active{color:var(--teal);border-bottom:2px solid var(--teal);padding-bottom:6px}

/* hero */
.hero{left:0;top:140px;width:1200px;height:540px;background:linear-gradient(100deg,#c9b48a 0%,#d9d1b8 30%,#bfd3df 60%,#9fc1d6 100%)}
.hero-title{left:640px;top:232px;width:460px;font-size:46px;line-height:52px;font-weight:700;color:var(--white)}
.hero-btn{left:640px;top:480px}
.arrow{width:40px;height:40px;border-radius:50%;background:var(--teal)}

/* services */
.svc{width:240px;height:280px;background:linear-gradient(160deg,#5b6166,#3a4045);text-align:center;color:var(--white)}
.svc h3{font-size:17px;font-weight:700;margin-top:40px;line-height:22px;padding:0 18px}
.svc svg{margin-top:14px}
.svc .btn{position:absolute;left:50%;bottom:32px;transform:translateX(-50%)}

/* who we are */
.who-bg{left:0;top:1560px;width:1200px;height:560px}
.who-photo{left:164px;top:1664px;width:340px;height:340px;border-radius:50%;border:10px solid var(--white);background:radial-gradient(circle at 50% 40%,#e8ecef,#b7cfdc)}
.who-title{left:612px;top:1766px;font-size:36px;font-weight:900;color:var(--white)}
.who-text{left:612px;top:1828px;width:480px;font-size:13px;line-height:20px;color:var(--white)}
.who-btn{left:612px;top:1964px}

/* features */
.feat-bg{left:0;top:2090px;width:1200px;height:400px;background:var(--lav)}
.feat{top:2192px;width:300px;height:300px;background:var(--white);text-align:center;box-shadow:0 4px 14px rgba(0,0,0,.06)}
.feat .ico{width:110px;height:110px;border-radius:50%;border:1px solid #ddd;margin:36px auto 26px;display:flex;align-items:center;justify-content:center}
.feat h4{font-size:22px;font-weight:900}
.feat p{font-size:13px;color:var(--grey);line-height:18px;margin-top:8px;padding:0 40px}

/* products */
.prod{top:2688px;width:260px;text-align:center}
.prod .pic{width:260px;height:260px;border-radius:50%;border:6px solid var(--white);box-shadow:0 0 0 2px #eee}
.prod h4{font-size:22px;font-weight:900;margin-top:30px}
.prod p{font-size:13px;color:var(--grey);line-height:18px;margin-top:6px;padding:0 30px}
.prod .btn{margin-top:20px}
.chev{top:2900px}

/* hands */
.band{left:0;top:3200px;width:1200px;height:460px;background:linear-gradient(90deg,#8fb8b0 0%,#d7b39a 45%,#9fb7c6 100%)}

/* testimonials */
.quote{top:3836px;width:230px}
.stars{color:var(--teal);font-size:16px;letter-spacing:2px}
.quote p{font-size:13px;line-height:18px;color:#444;margin-top:12px}
.quote h5{font-size:17px;font-weight:900;margin-top:18px}
.quote small{font-size:12px;color:#999}

/* footer */
.footer{left:0;top:4192px;width:1200px;height:392px;background:var(--footer);color:var(--white)}
.fcol{top:4240px}
.fcol h6{font-size:16px;font-weight:900;letter-spacing:.5px;margin-bottom:22px}
.fcol li{list-style:none;font-size:13px;line-height:20px;color:#ddd}
.email{width:260px;height:48px;background:var(--white);color:#888;font-size:13px;padding:16px 14px}
.subscribe{background:var(--red);color:var(--white);font-size:13px;font-weight:700;padding:14px 18px;margin-top:16px;display:inline-block}
.fline{left:112px;top:4512px;width:976px;height:1px;background:#333}
.copy{left:0;top:4538px;width:1200px;text-align:center;font-size:13px;color:#ddd}
</style>
</head>
<body>

<!-- top bar -->
<div class="abs topbar"></div>
<div class="abs topbar-accent"></div>
<div class="abs social" style="left:48px"></div>
<div class="abs social" style="left:80px"></div>
<div class="abs social" style="left:112px"></div>
<div class="abs social" style="left:144px"></div>
<div class="abs call">Call us Today: <b>+1 888 888 8888</b></div>
<div class="abs tab" style="left:688px">BOOK NURSES</div>
<div class="abs tab" style="left:904px">BOOK HOME VISIT</div>

<!-- navigation -->
<div class="abs logo">LUMORA</div>
<nav class="abs menu">
  <span class="active">Home</span><span>About us</span><span>Services</span><span>Product</span><span>Reviews</span><span>Contact us</span><span>Cart : $0.00</span>
</nav>

<!-- hero -->
<div class="abs hero" role="img" aria-label="Woman with raised arms in a sunny field by the sea"></div>
<div class="abs hero-title">Hire of medical equipments including beds and wheelchairs</div>
<div class="abs hero-btn btn">Learn more</div>
<div class="abs arrow" style="left:-8px;top:390px"><svg width="40" height="40"><path d="M24 13 L16 20 L24 27" stroke="#fff" stroke-width="3" fill="none"/></svg></div>
<div class="abs arrow" style="left:1168px;top:390px"><svg width="40" height="40"><path d="M16 13 L24 20 L16 27" stroke="#fff" stroke-width="3" fill="none"/></svg></div>

<!-- services -->
<h2 class="section-title" style="top:770px">SERVICES WE PROVIDED ARE</h2>

<div class="abs svc" style="left:112px;top:864px" role="img" aria-label="Blood testing service photo">
  <h3>Blood testing</h3>
  <svg width="60" height="60" viewBox="0 0 60 60" fill="none" stroke="#fff" stroke-width="2"><path d="M30 8 C20 24 16 30 16 38 a14 14 0 0 0 28 0 C44 30 40 24 30 8Z"/><path d="M24 40 a6 6 0 0 0 6 6"/></svg>
  <span class="btn">Learn more</span>
</div>
<div class="abs svc" style="left:358px;top:864px" role="img" aria-label="Laboratory analysis photo">
  <h3>Laboratory analysis</h3>
  <svg width="60" height="60" viewBox="0 0 60 60" fill="none" stroke="#fff" stroke-width="2"><path d="M24 8 h12 M26 8 v16 L14 48 h32 L34 24 V8"/><path d="M20 38 h20"/></svg>
  <span class="btn">Learn more</span>
</div>
<div class="abs svc" style="left:604px;top:864px" role="img" aria-label="IV therapy photo">
  <h3>IV therapy</h3>
  <svg width="60" height="60" viewBox="0 0 60 60" fill="none" stroke="#fff" stroke-width="2"><path d="M12 48 L40 20 M34 14 L46 26 M40 8 L52 20 M18 42 L10 50 M22 30 l8 8 M28 24 l8 8"/></svg>
  <span class="btn">Learn more</span>
</div>
<div class="abs svc" style="left:850px;top:864px" role="img" aria-label="IV infusion drip photo">
  <h3>IV infusion drips</h3>
  <svg width="60" height="60" viewBox="0 0 60 60" fill="none" stroke="#fff" stroke-width="2"><rect x="18" y="6" width="24" height="30" rx="4"/><path d="M30 36 v8 M26 44 h8 v6 h-8z M30 50 v6"/><path d="M22 22 h16"/></svg>
  <span class="btn">Learn more</span>
</div>

<div class="abs svc" style="left:112px;top:1160px" role="img" aria-label="Phlebotomy services photo">
  <h3>Phlebotomy services</h3>
  <svg width="60" height="60" viewBox="0 0 60 60" fill="none" stroke="#fff" stroke-width="2"><path d="M10 40 h40 v10 H10z"/><path d="M30 8 C24 18 22 22 22 26 a8 8 0 0 0 16 0 C38 22 36 18 30 8Z"/></svg>
  <span class="btn">Learn more</span>
</div>
<div class="abs svc" style="left:358px;top:1160px" role="img" aria-label="Nurse on a home care visit photo">
  <h3>Nurses for Home care services</h3>
  <svg width="60" height="60" viewBox="0 0 60 60" fill="none" stroke="#fff" stroke-width="2"><path d="M10 30 L30 12 L50 30 M16 26 V50 H44 V26"/><path d="M30 32 v10 M25 37 h10"/></svg>
  <span class="btn">Learn more</span>
</div>
<div class="abs svc" style="left:604px;top:1160px" role="img" aria-label="Patient repatriation travel photo">
  <h3>Patient repatriation services to their...</h3>
  <svg width="60" height="60" viewBox="0 0 60 60" fill="none" stroke="#fff" stroke-width="2"><path d="M8 34 L52 20 L50 28 L30 34 L22 48 H16 L20 36 L10 38Z"/></svg>
  <span class="btn">Learn more</span>
</div>
<div class="abs svc" style="left:850px;top:1160px" role="img" aria-label="Medical equipment for hire photo">
  <h3>Hire of medica equipments including</h3>
  <svg width="60" height="60" viewBox="0 0 60 60" fill="none" stroke="#fff" stroke-width="2"><circle cx="26" cy="40" r="12"/><circle cx="26" cy="12" r="4"/><path d="M26 18 v14 h14 l6 12"/></svg>
  <span class="btn">Learn more</span>
</div>

<!-- who we are -->
<svg class="abs who-bg" viewBox="0 0 1200 560" preserveAspectRatio="none" aria-hidden="true">
  <path d="M0 40 C300 -10 600 10 800 50 C1000 90 1100 60 1200 30 V520 C900 580 700 520 400 540 C200 552 80 530 0 520Z" fill="#86cae7"/>
</svg>
<div class="abs who-photo" role="img" aria-label="Smiling nurse with stethoscope"></div>
<div class="abs who-title">WHO WE ARE</div>
<div class="abs who-text">Lorem ipsum dolor sit amet, consectetur adipiscing elit, sed do eiusmod tempor incididunt ut labore et dolore magna aliqua. Ut enim ad minim veniam, quis nostrud exercitation ullamco laboris nisi ut aliquip ex ea commodo consequat. Duis aute irure dolor in reprehenderit in voluptate velit esse cillum dolore eu fugiat nulla pariatur. Excepteur sint occaecat cupidatat non proident, sunt in culpa qui officia.</div>
<div class="abs who-btn btn">Learn more</div>

<!-- feature boxes -->
<div class="abs feat-bg"></div>
<div class="abs feat" style="left:112px">
  <div class="ico"><svg width="56" height="56" viewBox="0 0 56 56" fill="none" stroke="#444" stroke-width="2"><path d="M14 6 C14 22 42 34 42 50 M42 6 C42 22 14 34 14 50"/><path d="M18 14 h20 M22 22 h12 M22 34 h12 M18 42 h20"/></svg></div>
  <h4>Lorem ipsum dolor</h4><p>Lorem ipsum dolor sit amet, conse ctetur adipiscing elit, sed</p>
</div>
<div class="abs feat" style="left:450px">
  <div class="ico"><svg width="56" height="56" viewBox="0 0 56 56" fill="none" stroke="#444" stroke-width="2"><rect x="16" y="6" width="24" height="28" rx="4"/><path d="M28 34 v8 M24 42 h8 v6 h-8z M20 18 h16"/></svg></div>
  <h4>Lorem ipsum dolor</h4><p>Lorem ipsum dolor sit amet, conse ctetur adipiscing elit, sed</p>
</div>
<div class="abs feat" style="left:788px">
  <div class="ico"><svg width="56" height="56" viewBox="0 0 56 56" fill="none" stroke="#444" stroke-width="2"><path d="M28 8 C22 18 20 22 20 26 a8 8 0 0 0 16 0 C36 22 34 18 28 8Z"/><path d="M8 44 c8 -6 14 -6 20 0 h12 l8 -6"/></svg></div>
  <h4>Lorem ipsum dolor</h4><p>Lorem ipsum dolor sit amet, conse ctetur adipiscing elit, sed</p>
</div>

<!-- featured products -->
<h2 class="section-title" style="top:2594px">FEATURED PRODUCT</h2>
<div class="abs prod" style="left:142px">
  <div class="pic" role="img" aria-label="Patient in a wheelchair" style="background:linear-gradient(160deg,#dfe6ea,#a9bdc8)"></div>
  <h4>Lorem ipsum dolor</h4><p>Lorem ipsum dolor sit amet, conse ctetur adipiscing elit, sed</p>
  <span class="btn pale">Learn more</span>
</div>
<div class="abs prod" style="left:470px">
  <div class="pic" role="img" aria-label="Hospital bed in a care room" style="background:linear-gradient(160deg,#e9d6c6,#b7a595)"></div>
  <h4>Lorem ipsum dolor</h4><p>Lorem ipsum dolor sit amet, conse ctetur adipiscing elit, sed</p>
  <span class="btn">Learn more</span>
</div>
<div class="abs prod" style="left:798px">
  <div class="pic" role="img" aria-label="Vitamin supplement capsules and leaves" style="background:linear-gradient(160deg,#f1ecd6,#c9b36a)"></div>
  <h4>Lorem ipsum dolor</h4><p>Lorem ipsum dolor sit amet, conse ctetur adipiscing elit, sed</p>
  <span class="btn pale">Learn more</span>
</div>
<svg class="abs chev" style="left:48px" width="24" height="30"><path d="M18 4 L6 15 L18 26" stroke="#999" stroke-width="3" fill="none"/></svg>
<svg class="abs chev" style="left:1128px" width="24" height="30"><path d="M6 4 L18 15 L6 26" stroke="#999" stroke-width="3" fill="none"/></svg>

<!-- team band -->
<div class="abs band" role="img" aria-label="Medical team joining hands together"></div>

<!-- testimonials -->
<h2 class="section-title" style="top:3746px">OUR TESTIMONIALS</h2>
<div class="abs quote" style="left:108px"><div class="stars">★★★★★</div><p>"Lorem ipsum dolor sit amet, consectetur adipiscing elit, sed do eiusmod tempor incididunt ut labore et dolore magna aliqua. Ut enim ad minim veniam, quis nostrud exercitation ullamco laboris nisi ut aliquip"</p><h5>John doe</h5><small>Company name</small></div>
<div class="abs quote" style="left:368px"><div class="stars">★★★★★</div><p>"Lorem ipsum dolor sit amet, consectetur adipiscing elit, sed do eiusmod tempor incididunt ut labore et dolore magna aliqua. Ut enim ad minim veniam, quis nostrud exercitation ullamco laboris nisi ut aliquip"</p><h5>John doe</h5><small>Company name</small></div>
<div class="abs quote" style="left:628px"><div class="stars">★★★★★</div><p>"Lorem ipsum dolor sit amet, consectetur adipiscing elit, sed do eiusmod tempor incididunt ut labore et dolore magna aliqua. Ut enim ad minim veniam, quis nostrud exercitation ullamco laboris nisi ut aliquip"</p><h5>John doe</h5><small>Company name</small></div>
<div class="abs quote" style="left:888px"><div class="stars">★★★★★</div><p>"Lorem ipsum dolor sit amet, consectetur adipiscing elit, sed do eiusmod tempor incididunt ut labore et dolore magna aliqua. Ut enim ad minim veniam, quis nostrud exercitation ullamco laboris nisi ut aliquip"</p><h5>John doe</h5><small>Company name</small></div>
<svg class="abs" style="left:40px;top:3946px" width="24" height="30"><path d="M18 4 L6 15 L18 26" stroke="#222" stroke-width="3" fill="none"/></svg>
<svg class="abs" style="left:1136px;top:3946px" width="24" height="30"><path d="M6 4 L18 15 L6 26" stroke="#222" stroke-width="3" fill="none"/></svg>

<!-- footer -->
<footer class="abs footer"></footer>
<div class="abs fcol" style="left:112px"><h6>QUICK LINKS</h6><ul><li>Home</li><li>About</li><li>Services</li><li>Product</li><li>Reviews</li><li>Contact us</li></ul></div>
<div class="abs fcol" style="left:324px;width:220px"><h6>CONTACT US</h6><ul><li>123, Lorem ipsum dolor sit amet,<br>consectetur</li><li style="margin-top:14px">+1 888 888 8888</li><li style="margin-top:14px">hello@lumoraclinic.com</li></ul></div>
<div class="abs fcol" style="left:632px"><h6>SERVICES</h6><ul><li>Blood testing</li><li>laboratory analysis</li><li>IV therapy</li><li>IV infusion drips</li><li>phlebotomy services</li><li>More</li></ul></div>
<div class="abs fcol" style="left:832px"><h6>NEWSLETTER</h6><div class="email">Email address</div><span class="subscribe">Subscribe</span></div>
<div class="abs fline"></div>
<div class="abs copy">© Copyright 2020 Company name | All Right Reserved</div>

</body>
</html>
```